Copper Lattice of Brave Movers

Hi - I would like your help transforming my (terrible) drawing into a graphic that pops -using hex colors I'll give you - so that I can put it into stationary and on t-shirts or tote bags. My company, the Tundrel Institute, trains social change leaders (from the sectors in the periodic table) on how to lead large-scale change. I have this vision - the "periodic table" but these are the sectors that my clients work in. If you are having trouble reading my writing, I apologize. Our hex colors are: #114769, #76984C, #80B5CF (Seagull), #8F2C63 and Rangoon Black #191919. You don't need to use all of them, but it'd be good to be consistent with our overall branding. If you can't read my writing, I will send correct spelling. The "Tundrel" with the flowers on the bottom is for a separate design bid.

Target Market(s)

nonprofit, social entrepreneurs, philanthropy, leaders

Requirements
Must have
• clean, readable font. alignment to look like periodic table of elements. heart icon for love, cat face for cats.

```html
<!DOCTYPE html>
<html lang="en">
<head>
<meta charset="utf-8">
<title>Copper Lattice of Brave Movers</title>
<link rel="stylesheet" href="https://fonts.googleapis.com/css2?family=Arimo:wght@400;700&display=swap">
<style>
  :root {
    --ink: #231f20;
    --paper: #ffffff;
    --mist: #d7e4ed;
    --teal: #0e6983;
    --seagull: #80b5cf;
    --navy: #114769;
    --plum: #8f2c63;
    --cell: 164px;
    --rule: 3px;
  }
  * { box-sizing: border-box; margin: 0; padding: 0; }
  html, body { width: 1117px; height: 1200px; overflow: hidden; background: var(--paper); }
  body { position: relative; font-family: "Arimo", Helvetica, Arial, sans-serif; color: var(--ink); }

  .table {
    position: absolute;
    left: 62px;
    display: grid;
    grid-template-columns: repeat(6, var(--cell));
    grid-auto-rows: var(--cell);
  }
  .table--sectors { top: 128px; }
  .table--values { top: 846px; grid-template-columns: repeat(5, var(--cell)); }

  .element {
    position: relative;
    box-shadow: 0 0 0 var(--rule) var(--ink), inset 0 0 0 var(--rule) var(--ink);
    text-align: center;
  }
  .element--empty { box-shadow: none; }
  .element--mist { background: var(--mist); color: var(--ink); }
  .element--teal { background: var(--teal); color: #fff; }
  .element--seagull { background: var(--seagull); color: var(--ink); }
  .element--navy { background: var(--navy); color: #fff; }
  .element--plum { background: var(--plum); color: #fff; }

  .element__symbol {
    position: absolute;
    left: 0; right: 0; top: 14px;
    font-weight: 700;
    font-size: 76px;
    line-height: 76px;
    letter-spacing: -1px;
  }
  .element__icon {
    position: absolute;
    left: 50%; top: 20px;
    transform: translateX(-50%);
  }
  .element__name {
    position: absolute;
    left: 0; right: 0; top: 94px; height: 50px;
    display: flex; align-items: center; justify-content: center;
    font-size: 22px;
    line-height: 23px;
    letter-spacing: 0.2px;
  }
  .table--values .element__name { top: 104px; height: 40px; }

  .values-title {
    position: absolute;
    left: 64px; top: 1028px;
    font-weight: 700;
    font-size: 100px;
    line-height: 110px;
    letter-spacing: -3px;
  }
</style>
</head>
<body>
  <main>
    <section class="table table--sectors" aria-label="Sectors">
      <div class="element element--mist"><span class="element__symbol">Av</span><span class="element__name">Anti<br>Violence</span></div>
      <div class="element element--empty"></div>
      <div class="element element--empty"></div>
      <div class="element element--empty"></div>
      <div class="element element--empty"></div>
      <div class="element element--mist"><span class="element__symbol">B</span><span class="element__name">Belonging</span></div>

      <div class="element element--teal"><span class="element__symbol">Ec</span><span class="element__name">Early<br>Childhood</span></div>
      <div class="element element--teal"><span class="element__symbol">Cc</span><span class="element__name">Climate<br>Change</span></div>
      <div class="element element--teal"><span class="element__symbol">Ej</span><span class="element__name">Environmental<br>Justice</span></div>
      <div class="element element--teal"><span class="element__symbol">Hs</span><span class="element__name">Human<br>Services</span></div>
      <div class="element element--teal"><span class="element__symbol">Hs</span><span class="element__name">Health<br>Care</span></div>
      <div class="element element--teal"><span class="element__symbol">H</span><span class="element__name">Housing</span></div>

      <div class="element element--seagull"><span class="element__symbol">Ed</span><span class="element__name">Education</span></div>
      <div class="element element--seagull"><span class="element__symbol">As</span><span class="element__name">After<br>School</span></div>
      <div class="element element--seagull"><span class="element__symbol">Si</span><span class="element__name">Socail<br>Justice</span></div>
      <div class="element element--seagull"><span class="element__symbol">Cr</span><span class="element__name">Civil<br>Rights</span></div>
      <div class="element element--seagull"><span class="element__symbol">He</span><span class="element__name">Health<br>Equity</span></div>
      <div class="element element--seagull"><span class="element__symbol">J</span><span class="element__name">Jobs</span></div>

      <div class="element element--navy"><span class="element__symbol">Aw</span><span class="element__name">Animal<br>Welfare</span></div>
      <div class="element element--navy"><span class="element__symbol">Av</span><span class="element__name">Anti<br>Violence</span></div>
      <div class="element element--navy"><span class="element__symbol">Rj</span><span class="element__name">Anti<br>Violence</span></div>
      <div class="element element--navy">
        <svg class="element__icon" width="70" height="66" viewBox="0 0 70 66" aria-hidden="true">
          <path d="M12 4 C20 10 26 12 35 12 C44 12 50 10 58 4 C59 14 60 22 62 30 C66 38 66 46 62 52 C56 60 46 62 35 62 C24 62 14 60 8 52 C4 46 4 38 8 30 C10 22 11 14 12 4 Z" fill="none" stroke="#fff" stroke-width="6" stroke-linejoin="round"/>
        </svg>
        <span class="element__name">Cats</span>
      </div>
      <div class="element element--navy"><span class="element__symbol">Bh</span><span class="element__name">Behavioral<br>Health</span></div>
      <div class="element element--navy"><span class="element__symbol">Ig</span><span class="element__name">Inter-<br>generations</span></div>
    </section>

    <section class="table table--values" aria-label="Values">
      <div class="element element--plum">
        <svg class="element__icon" width="76" height="68" viewBox="0 0 76 68" aria-hidden="true" style="top:30px">
          <path d="M38 62 C30 50 6 40 6 22 C6 10 16 4 24 4 C31 4 36 8 38 14 C40 8 45 4 52 4 C60 4 70 10 70 22 C70 40 46 50 38 62 Z" fill="none" stroke="#fff" stroke-width="7" stroke-linejoin="round"/>
        </svg>
        <span class="element__name" style="top:98px">Love</span>
      </div>
      <div class="element element--plum"><span class="element__symbol">A</span><span class="element__name">Autenticity</span></div>
      <div class="element element--plum"><span class="element__symbol">Hm</span><span class="element__name">Humility</span></div>
      <div class="element element--plum"><span class="element__symbol">Au</span><span class="element__name">Authenticity</span></div>
      <div class="element element--plum"><span class="element__symbol">Ju</span><span class="element__name">Justice</span></div>
    </section>

    <h1 class="values-title">Values</h1>
  </main>
</body>
</html>
```